BrightOak Lending Needs a Stated Income Flyer

We need a flyer created for our Stated Income loan program, using the color scheme to match our company logo.
I've included a stock photo to be used and within that photo, we want Funded stamped in red on the blank poster board.
For the written part of the flyer, we want the word State Income in red.
On the bottom part (Contact Us), we want to make it possible for us to edit for any future loan officer we hire along the way to include their contact information.
We like the flyer for VeroCredit.
Industry/Entity Type
Loan

```html
<!DOCTYPE html>
<html lang="en">
<head>
<meta charset="utf-8">
<title>BrightOak Lending – Stated Income Flyer</title>
<link href="https://fonts.googleapis.com/css2?family=Oswald:wght@500;600&family=Roboto+Condensed:wght@300;400;700&family=Arimo:wght@700&display=swap" rel="stylesheet">
<style>
  :root {
    --navy: #1d3f8c;
    --navy-dark: #17336f;
    --red: #e3202a;
    --ink: #111111;
    --paper: #ffffff;
    --photo-light: #eeeae6;
    --photo-mid: #cbb8a8;
    --photo-dark: #3b3f4a;
    --house: #dde2ec;
  }
  * { margin: 0; padding: 0; box-sizing: border-box; }
  html, body { width: 856px; height: 1200px; overflow: hidden; background: var(--paper); }
  .flyer { position: relative; width: 856px; height: 1200px; background: var(--paper); color: var(--ink); font-family: "Roboto Condensed", sans-serif; }

  .hero-photo {
    position: absolute; left: 0; top: 0; width: 856px; height: 620px;
    background: linear-gradient(180deg, var(--photo-light) 0%, var(--photo-mid) 55%, var(--photo-dark) 100%);
  }
  .brand {
    position: absolute; right: 30px; top: 34px; display: flex; align-items: center; gap: 8px;
    font-family: "Oswald", sans-serif; font-weight: 500; font-size: 24px; color: var(--navy);
  }
  .brand-mark { width: 22px; height: 22px; background: var(--navy); }

  .sign-board {
    position: absolute; left: 126px; top: 292px; width: 390px; height: 266px;
    background: var(--paper); text-align: center; box-shadow: 0 4px 10px rgba(0,0,0,.2);
  }
  .sign-title { margin-top: 52px; font-family: "Oswald", sans-serif; font-weight: 600; font-size: 40px; color: var(--red); letter-spacing: .5px; }
  .sign-sub { font-family: "Times New Roman", serif; font-size: 34px; color: var(--ink); letter-spacing: 1px; }
  .sign-brand { margin-top: 28px; font-family: "Oswald", sans-serif; font-weight: 500; font-size: 22px; color: var(--navy); }

  .house-graphic {
    position: absolute; left: 250px; top: 660px; width: 330px; height: 420px;
    background: radial-gradient(ellipse at 50% 45%, var(--house) 0%, rgba(221,226,236,.35) 60%, rgba(255,255,255,0) 75%);
  }

  .program { position: absolute; left: 40px; top: 710px; width: 340px; }
  .program-title { font-family: "Oswald", sans-serif; font-weight: 600; font-size: 24px; line-height: 30px; }
  .program-note { width: 300px; text-align: center; font-weight: 700; font-size: 17px; line-height: 21px; }

  .rates { position: absolute; left: 528px; top: 728px; width: 300px; text-align: center; }
  .rates-title { font-family: "Oswald", sans-serif; font-weight: 600; font-size: 24px; line-height: 30px; }
  .rates-note { font-weight: 700; font-size: 16px; line-height: 20px; }

  .feature-list { position: absolute; list-style: none; font-weight: 300; font-size: 22px; line-height: 30px; }
  .feature-list li { position: relative; padding-left: 28px; }
  .feature-list li::before {
    content: ""; position: absolute; left: 2px; top: 8px; width: 13px; height: 13px; background: var(--navy);
  }
  .feature-list.left { left: 72px; top: 800px; width: 360px; }
  .feature-list.right { left: 532px; top: 802px; width: 250px; }

  .contact { position: absolute; left: 540px; top: 988px; width: 240px; text-align: center; }
  .contact-title { font-family: "Arimo", sans-serif; font-weight: 700; font-size: 32px; color: var(--navy); margin-left: -24px; margin-bottom: 6px; }
  .contact-line { font-family: "Arimo", sans-serif; font-weight: 700; font-size: 15px; line-height: 21px; white-space: nowrap; }

  .legal {
    position: absolute; left: 30px; top: 1128px; width: 796px; text-align: center;
    font-size: 11px; line-height: 14px; color: var(--ink);
  }
</style>
</head>
<body>
<main class="flyer">
  <section class="hero-photo" role="img" aria-label="Stock photo of a cheering group of business people holding up a blank poster board"></section>
  <div class="brand"><span class="brand-mark"></span>BrightOak Lending</div>
  <div class="sign-board">
    <p class="sign-title">STATED INCOME</p>
    <p class="sign-sub">FAST &amp; EASY</p>
    <p class="sign-brand">BrightOak Lending</p>
  </div>

  <div class="house-graphic" role="img" aria-label="Large light silver house outline with a check mark"></div>

  <div class="program">
    <h2 class="program-title">PURCHASE &amp; CASH OUT REFINANC</h2>
    <p class="program-note">Non-owner SFR/Condo/2-4 Units<br>5+ Units &amp; Commercial – Ask for Details</p>
  </div>

  <div class="rates">
    <h2 class="rates-title">RATES AS LOW AS 6.49%</h2>
    <p class="rates-note">3 &amp; 5 Year Fixed ARM – 30 Year Amortization</p>
  </div>

  <ul class="feature-list left">
    <li>NO Tax Returns</li>
    <li>NO 4506-T</li>
    <li>NO Cash-Out Restrictions</li>
    <li>NO Cash Reserves Required</li>
    <li>NO Limit on Number of Properties owned or financed</li>
    <li>NO DTI Calculation</li>
    <li>NO Seasoned Funds – No Asset</li>
    <li>Disclosures (Purchase)</li>
  </ul>

  <ul class="feature-list right">
    <li>Max Rebate 2%</li>
    <li>Max 70% Loan-to-value</li>
    <li>650 Min Credit Score</li>
    <li>Loan Amounts $100,000 to $2,000,000</li>
  </ul>

  <div class="contact">
    <h2 class="contact-title">Contact Us</h2>
    <p class="contact-line">Marcus Ellery</p>
    <p class="contact-line">888-555-0142</p>
    <p class="contact-line">marcus@brightoaklend.com</p>
    <p class="contact-line">BRE #00000000</p>
  </div>

  <p class="legal">Intended for mortgage professional only and not intended for consumer use as defined by Section 226.24 of Regulation Z. Financing subject to credit evaluation, approval of collateral and other requirements. Non-regulation Z covered loans. Terms and conditions subject to change without notice. BrightOak Lending is licensed by the California Bureau of Real Estate, BRE License No. 00000000 NMLS ID 000000, 4200 Harbor View Drive, Suite 210, Irvine, CA 92600.</p>
</main>
</body>
</html>
```